Fun & Healthy Dog Treat Business Needs a Business & Loyalty Card

We need a business card design for a business that provides healthy dog products.

The design should communicate a healthy aspect and should communicate that the business focuses on healthy produce.

We would like some aspects if not all of our current logo to appear on the card.

We would also like a two sided card with the back of the card being able to be used as a loyalty program where after purchasing 7 items the buyer receives a free gift. There should be a way of identifying how many purchases a customer has made and if possible enable at least 4 - 5 gives be able to be given on one card. ie make 7 purchases and receive a give, to be able to be done 4 - 5 times before they need to be given a new card.

Rather than the focus be solely on dog treats we would like the card's focus to be a bit wider should we decide to enter other markets in the future and therefore not mention dog treats.

We want the card to be colourful while still retaining a very healthy aspect.

We also need the card to have pictures such as a dog or dogs head that enable us to determine how many items a customer has purchase before we give them a free gift.

Please see our website for further details regarding our business including contact details. www.wrenfieldpantry.com.au

Target Market(s)

Dog lovers who are health concious

Industry/Entity Type

Pet

Contact Information for Business Card

Products for Healthy Dogs
Web Address - www.wrenfieldpantry.com.au
Email address - info@wrenfieldpantry.com.au

Font styles to use
Serif

Colors
acd037
f04a50

Requirements
Must have
• Wrenfield Pantry
• Products for Healthy Dogs
• Web Address - www.wrenfieldpantry.com.au
• Email address - info@wrenfieldpantry.com.au
• Mobile Number - 0417 358 619
Nice to have
• Part of our current logo
• Blend in with current logo but not include the words healthy dog treats
• The flip side of the card should have a Loyalty Program where when you purchase 7 products you receive a free gift.
Should not have
• Should not include the words healthy dog treats
• Should not have the fixed line phone number

```html
<!DOCTYPE html>
<html lang="en">
<head>
<meta charset="utf-8">
<title>Wrenfield Pantry – Business &amp; Loyalty Card</title>
<link rel="stylesheet" href="https://fonts.googleapis.com/css2?family=Noto+Serif:wght@400;600;700&display=swap">
<style>
  :root {
    --page: #f1eadf;
    --card: #ffffff;
    --red: #f04a50;
    --green: #acd037;
    --ink: #1a1a1a;
    --rule: #1f2233;
  }
  * { box-sizing: border-box; margin: 0; padding: 0; }
  html, body {
    width: 1189px; height: 1200px; overflow: hidden;
    background: var(--page);
    font-family: "Noto Serif", Georgia, serif;
    color: var(--ink);
  }
  .card {
    position: absolute; left: 167px;
    width: 855px; height: 488px;
    background: var(--card);
    border-radius: 20px;
    border: 1px solid #e3dccf;
  }
  .card--front { top: 67px; }
  .card--back { top: 626px; }

  .brand { position: absolute; display: flex; align-items: center; gap: 18px; }
  .brand__dot { width: 74px; height: 74px; border-radius: 50%; background: var(--green); flex: none; }
  .brand__name { font-weight: 700; color: var(--red); font-size: 40px; line-height: 1.1; }
  .tagline { position: absolute; font-size: 18px; color: var(--ink); letter-spacing: 0.5px; }

  .card--front .brand { left: 38px; top: 170px; width: 360px; }
  .card--front .tagline { left: 38px; top: 270px; width: 360px; text-align: center; }

  .card--back .brand { left: 0; right: 0; top: 30px; justify-content: center; gap: 14px; }
  .card--back .brand__dot { width: 52px; height: 52px; }
  .card--back .brand__name { font-size: 38px; }
  .card--back .tagline { left: 0; right: 0; top: 92px; text-align: center; }

  .divider { position: absolute; left: 418px; top: 113px; width: 2px; height: 271px; background: var(--rule); }
  .details { position: absolute; left: 449px; top: 110px; }
  .details__name { color: var(--red); font-size: 37px; font-weight: 600; line-height: 1.05; }
  .details__role { font-size: 26px; line-height: 1.1; }
  .details__address { margin-top: 34px; font-size: 25px; line-height: 1.25; }
  .contact { margin-top: 16px; list-style: none; font-size: 23px; line-height: 1.3; }
  .contact li { display: flex; align-items: center; gap: 12px; }
  .contact svg { width: 26px; height: 26px; flex: none; }
  .contact .web { color: var(--red); margin-top: 8px; }

  .stamps {
    position: absolute; left: 0; right: 0; top: 140px;
    display: grid; grid-template-columns: repeat(7, 44px);
    justify-content: center; column-gap: 40px; row-gap: 10px;
  }
  .stamp { position: relative; width: 44px; height: 40px; }
  .stamp svg { width: 44px; height: 40px; display: block; }
  .stamp__label {
    position: absolute; left: 0; right: 0; top: 17px;
    text-align: center; font-size: 12px; line-height: 1; letter-spacing: 0.5px;
  }
  .back-web { position: absolute; left: 0; right: 0; top: 410px; text-align: center; font-size: 23px; }
</style>
</head>
<body>

<svg width="0" height="0" style="position:absolute" aria-hidden="true">
  <defs>
    <path id="cloche" d="M34 0h10v5A39 38 0 0 1 78 42v31Q39 78 0 73V42A39 38 0 0 1 34 5z" fill="#f04a50"/>
  </defs>
</svg>

<section class="card card--front">
  <div class="brand">
    <span class="brand__dot"></span>
    <span class="brand__name">Wrenfield<br>Pantry</span>
  </div>
  <p class="tagline">Products for Healthy Dogs</p>
  <div class="divider"></div>
  <div class="details">
    <p class="details__name">Employee Name</p>
    <p class="details__role">Owner</p>
    <p class="details__address">PO Box 4815<br>HARLOW BAY VIC 3041</p>
    <ul class="contact">
      <li>
        <svg viewBox="0 0 26 26" aria-hidden="true"><rect width="26" height="26" rx="4" fill="#f04a50"/><rect x="8" y="4" width="10" height="18" rx="2" fill="none" stroke="#fff" stroke-width="2"/><rect x="10" y="7" width="6" height="5" fill="#fff"/></svg>
        +0417 358 619
      </li>
      <li>
        <svg viewBox="0 0 26 26" aria-hidden="true"><rect width="26" height="26" rx="4" fill="#f04a50"/><rect x="4" y="7" width="18" height="12" fill="none" stroke="#fff" stroke-width="2"/><path d="M4 7 L13 14 L22 7 M4 19 L10.5 12.5 M22 19 L15.5 12.5" fill="none" stroke="#fff" stroke-width="1.6"/></svg>
        info@wrenfieldpantry.com.au
      </li>
      <li class="web">www.wrenfieldpantry.com.au</li>
    </ul>
  </div>
</section>

<section class="card card--back">
  <div class="brand">
    <span class="brand__dot"></span>
    <span class="brand__name">Wrenfield Pantry</span>
  </div>
  <p class="tagline">Products for Healthy Dogs</p>
  <div class="stamps">
    <div class="stamp"><svg viewBox="0 0 78 75" aria-hidden="true"><use href="#cloche"/></svg></div>
    <div class="stamp"><svg viewBox="0 0 78 75" aria-hidden="true"><use href="#cloche"/></svg></div>
    <div class="stamp"><svg viewBox="0 0 78 75" aria-hidden="true"><use href="#cloche"/></svg></div>
    <div class="stamp"><svg viewBox="0 0 78 75" aria-hidden="true"><use href="#cloche"/></svg></div>
    <div class="stamp"><svg viewBox="0 0 78 75" aria-hidden="true"><use href="#cloche"/></svg></div>
    <div class="stamp"><svg viewBox="0 0 78 75" aria-hidden="true"><use href="#cloche"/></svg></div>
    <div class="stamp"><svg viewBox="0 0 78 75" aria-hidden="true"><use href="#cloche"/></svg><span class="stamp__label">Free</span></div>

    <div class="stamp"><svg viewBox="0 0 78 75" aria-hidden="true"><use href="#cloche"/></svg></div>
    <div class="stamp"><svg viewBox="0 0 78 75" aria-hidden="true"><use href="#cloche"/></svg></div>
    <div class="stamp"><svg viewBox="0 0 78 75" aria-hidden="true"><use href="#cloche"/></svg></div>
    <div class="stamp"><svg viewBox="0 0 78 75" aria-hidden="true"><use href="#cloche"/></svg></div>
    <div class="stamp"><svg viewBox="0 0 78 75" aria-hidden="true"><use href="#cloche"/></svg></div>
    <div class="stamp"><svg viewBox="0 0 78 75" aria-hidden="true"><use href="#cloche"/></svg></div>
    <div class="stamp"><svg viewBox="0 0 78 75" aria-hidden="true"><use href="#cloche"/></svg><span class="stamp__label">Free</span></div>

    <div class="stamp"><svg viewBox="0 0 78 75" aria-hidden="true"><use href="#cloche"/></svg></div>
    <div class="stamp"><svg viewBox="0 0 78 75" aria-hidden="true"><use href="#cloche"/></svg></div>
    <div class="stamp"><svg viewBox="0 0 78 75" aria-hidden="true"><use href="#cloche"/></svg></div>
    <div class="stamp"><svg viewBox="0 0 78 75" aria-hidden="true"><use href="#cloche"/></svg></div>
    <div class="stamp"><svg viewBox="0 0 78 75" aria-hidden="true"><use href="#cloche"/></svg></div>
    <div class="stamp"><svg viewBox="0 0 78 75" aria-hidden="true"><use href="#cloche"/></svg></div>
    <div class="stamp"><svg viewBox="0 0 78 75" aria-hidden="true"><use href="#cloche"/></svg><span class="stamp__label">Free</span></div>

    <div class="stamp"><svg viewBox="0 0 78 75" aria-hidden="true"><use href="#cloche"/></svg></div>
    <div class="stamp"><svg viewBox="0 0 78 75" aria-hidden="true"><use href="#cloche"/></svg></div>
    <div class="stamp"><svg viewBox="0 0 78 75" aria-hidden="true"><use href="#cloche"/></svg></div>
    <div class="stamp"><svg viewBox="0 0 78 75" aria-hidden="true"><use href="#cloche"/></svg></div>
    <div class="stamp"><svg viewBox="0 0 78 75" aria-hidden="true"><use href="#cloche"/></svg></div>
    <div class="stamp"><svg viewBox="0 0 78 75" aria-hidden="true"><use href="#cloche"/></svg></div>
    <div class="stamp"><svg viewBox="0 0 78 75" aria-hidden="true"><use href="#cloche"/></svg><span class="stamp__label">Free</span></div>

    <div class="stamp"><svg viewBox="0 0 78 75" aria-hidden="true"><use href="#cloche"/></svg></div>
    <div class="stamp"><svg viewBox="0 0 78 75" aria-hidden="true"><use href="#cloche"/></svg></div>
    <div class="stamp"><svg viewBox="0 0 78 75" aria-hidden="true"><use href="#cloche"/></svg></div>
    <div class="stamp"><svg viewBox="0 0 78 75" aria-hidden="true"><use href="#cloche"/></svg></div>
    <div class="stamp"><svg viewBox="0 0 78 75" aria-hidden="true"><use href="#cloche"/></svg></div>
    <div class="stamp"><svg viewBox="0 0 78 75" aria-hidden="true"><use href="#cloche"/></svg></div>
    <div class="stamp"><svg viewBox="0 0 78 75" aria-hidden="true"><use href="#cloche"/></svg><span class="stamp__label">Free</span></div>
  </div>
  <p class="back-web">www.wrenfieldpantry.com.au</p>
</section>

</body>
</html>
```